Corporate Trainning business needs PPT template for sales, reports and projects

Create a power point template with own design and rich in distinctness of our brand, logo and industry (corporate training). Enough slides templates to use for sales, reports and projects development: flowcharts, roadmaps, bullets, service categories, description box, title & subtitle slides, bar & pie charts, calendars, gantt, some basic shapes and icons (training, education, elearning, etc related).
Enclose: color palette, set of logo for different uses and ppt presentation with some ideas and slide templates. The ppt hope could help, but I trust in your experience and creativity.

Target Market(s)

Company training

Industry/Entity Type

Training - Education

Font styles to use
Sans Serif

Requirements
Nice to have
• Relative to training icons

```html
<!DOCTYPE html>
<html lang="en">
<head>
<meta charset="utf-8">
<title>Corvanta Presentation Template</title>
<link rel="stylesheet" href="https://fonts.googleapis.com/css2?family=Montserrat:wght@300;400;500;700;800&display=swap">
<style>
:root{
  --navy:#0b2b55;
  --yellow:#f2c300;
  --teal:#0a8aa8;
  --grey-text:#6b6f76;
  --body-text:#7b7f86;
  --backdrop:#c4c4c4;
  --white:#ffffff;
}
*{box-sizing:border-box;margin:0;padding:0}
html,body{width:948px;height:1200px;overflow:hidden}
body{background:var(--backdrop);font-family:'Montserrat',sans-serif;position:relative}

.slide{position:absolute;width:1280px;height:720px;background:var(--white);overflow:hidden;transform-origin:0 0}
.slide--hero{left:128px;top:75px;transform:scale(.5406)}
.slide--title-small{left:40px;top:661px;transform:scale(.3328)}
.slide--solutions{left:481px;top:661px;transform:scale(.3328)}
.slide--values{left:40px;top:915px;transform:scale(.3328)}
.slide--contact{left:481px;top:915px;transform:scale(.3328)}

/* brand name */
.brand{position:absolute;display:flex;align-items:center;gap:14px;color:var(--navy);font-weight:500}
.brand__dot{border-radius:50%;background:var(--yellow);flex:none}
.brand--large{left:68px;top:72px;font-size:66px}
.brand--large .brand__dot{width:70px;height:70px}
.brand--footer{left:32px;top:640px;font-size:38px;gap:10px}
.brand--footer .brand__dot{width:40px;height:40px}

/* photo areas */
.photo{position:absolute;border-radius:50%;overflow:hidden}
.photo--chart{left:585px;top:-704px;width:2208px;height:2208px;
  background:radial-gradient(circle at 45% 40%,#e9c9b0 0,#d8b59b 12%,transparent 26%),linear-gradient(160deg,#eef0f5 0%,#dfe3ec 45%,#c9cfdc 100%)}
.photo--towers{left:572px;top:-750px;width:2208px;height:2208px;
  background:linear-gradient(200deg,#c9d0d4 0%,#5e7278 35%,#22373c 65%,#3b4d52 100%)}
.tint{position:absolute}
.tint--teal{left:808px;top:0;width:180px;height:162px;background:rgba(10,138,168,.55);border-radius:0 0 60px 60px}
.tint--yellow{left:1085px;top:366px;width:195px;height:216px;background:rgba(242,195,0,.65);border-radius:60px 0 0 60px}

/* title panel */
.title-panel{position:absolute;left:0;top:224px;width:708px;height:270px;background:var(--navy);border-radius:0 100px 100px 0;padding:38px 0 0 70px;box-shadow:0 4px 8px rgba(0,0,0,.15)}
.title-panel__kicker{color:var(--yellow);font-weight:800;font-size:70px;line-height:1;letter-spacing:1px}
.title-panel__title{color:var(--yellow);font-weight:300;font-size:66px;line-height:1.12}
.title-panel__subtitle{color:var(--white);font-size:28px;margin-top:26px}
.slide-date{position:absolute;left:70px;top:572px;font-size:16px;color:var(--grey-text)}

.band{position:absolute;left:0;bottom:0;width:100%;height:48px;background:var(--teal);color:var(--white);font-size:15px;display:flex;align-items:center;justify-content:center}

/* content slides */
.heading{position:absolute;left:50px;top:52px;height:56px;display:flex;align-items:center;gap:28px;color:var(--navy);font-size:38px}
.heading::before{content:"";width:13px;height:56px;border-radius:7px;background:var(--yellow)}
.heading b{font-weight:700}
.page-footer{position:absolute;right:38px;top:650px;display:flex;align-items:center;gap:24px;font-size:13px;color:var(--grey-text)}
.page-footer__num{border-left:4px solid var(--teal);padding-left:18px;color:var(--yellow);font-weight:700;font-size:15px}

.badge{border-radius:50%;display:flex;align-items:center;justify-content:center}
.badge svg{fill:none;stroke:var(--white);stroke-width:1.8;stroke-linecap:round;stroke-linejoin:round}
.badge--navy{background:var(--navy)}
.badge--yellow{background:var(--yellow)}
.badge--teal{background:var(--teal)}

.solution{position:absolute;width:360px;text-align:center;display:flex;flex-direction:column;align-items:center}
.solution .badge{width:84px;height:84px}
.solution .badge svg{width:46px;height:46px}
.solution__title{margin-top:14px;font-size:28px;color:var(--navy)}
.solution__title b{font-weight:700}
.solution__text{margin-top:8px;font-size:16px;line-height:1.1;color:var(--body-text);width:320px}

.value{position:absolute;left:175px;display:flex;align-items:center;gap:26px;width:950px}
.value .badge{width:114px;height:114px;flex:none}
.value .badge svg{width:58px;height:58px}
.value__title{font-size:28px;color:var(--navy)}
.value__title b{font-weight:700}
.value__text{margin-top:12px;font-size:15px;line-height:1.15;color:var(--body-text);width:790px}

.contact{position:absolute;left:88px;top:428px}
.contact__title{font-size:26px;font-weight:700;color:var(--navy);margin-bottom:24px}
.contact__row{display:flex;align-items:center;gap:18px;font-size:18px;color:var(--grey-text);height:37px}
.contact__row svg{width:24px;height:24px;fill:none;stroke:var(--navy);stroke-width:2;stroke-linecap:round;stroke-linejoin:round}
.brand--contact{left:80px;top:280px;font-size:66px}
.brand--contact .brand__dot{width:70px;height:70px}
</style>
</head>
<body>

<!-- Hero title slide -->
<section class="slide slide--hero">
  <div class="photo photo--chart" role="img" aria-label="Photo of a hand with a blue pen drawing on a printed line chart"></div>
  <div class="tint tint--teal"></div>
  <div class="tint tint--yellow"></div>
  <div class="brand brand--large"><span class="brand__dot"></span>Corvanta</div>
  <div class="title-panel">
    <p class="title-panel__kicker">PRESENTATION</p>
    <p class="title-panel__title">Title Goes Here!</p>
    <p class="title-panel__subtitle">Presentation Subtitle Goes Here!</p>
  </div>
  <p class="slide-date">Saturday, August 13, 2022</p>
  <footer class="band">© 2022 Corvanta Learning, All rights reserved.</footer>
</section>

<!-- Title slide thumbnail -->
<section class="slide slide--title-small">
  <div class="photo photo--chart" role="img" aria-label="Photo of a hand with a blue pen drawing on a printed line chart"></div>
  <div class="tint tint--teal"></div>
  <div class="tint tint--yellow"></div>
  <div class="brand brand--large"><span class="brand__dot"></span>Corvanta</div>
  <div class="title-panel">
    <p class="title-panel__kicker">PRESENTATION</p>
    <p class="title-panel__title">Title Goes Here!</p>
    <p class="title-panel__subtitle">Presentation Subtitle Goes Here!</p>
  </div>
  <p class="slide-date">Saturday, August 13, 2022</p>
  <footer class="band">© 2022 Corvanta Learning, All rights reserved.</footer>
</section>

<!-- Solutions slide -->
<section class="slide slide--solutions">
  <h2 class="heading"><span><b>Corvanta</b> Solutions</span></h2>

  <div class="solution" style="left:67px;top:166px">
    <div class="badge badge--navy"><svg viewBox="0 0 24 24"><path d="M9 18h6M10 21h4M12 3a6 6 0 0 0-3.5 10.9c.6.5 1 1.2 1 2V16h5v-.1c0-.8.4-1.5 1-2A6 6 0 0 0 12 3z"/></svg></div>
    <p class="solution__title"><b>Heading</b> Goes Here</p>
    <p class="solution__text">Vivamus eu dui ex. Curabitur dapibus dignissim dui, in molest</p>
  </div>
  <div class="solution" style="left:460px;top:166px">
    <div class="badge badge--yellow"><svg viewBox="0 0 24 24"><path d="M14 4c3-1 6-1 6-1s0 3-1 6l-6 6-4-4 5-7zM9 11l-4 1-2 3 4 1M13 15l-1 4-3 2-1-4M15 9h.01"/></svg></div>
    <p class="solution__title"><b>Heading</b> Goes Here</p>
    <p class="solution__text">Vivamus eu dui ex. Curabitur dapibus dignissim dui, in molest</p>
  </div>
  <div class="solution" style="left:853px;top:166px">
    <div class="badge badge--teal"><svg viewBox="0 0 24 24"><circle cx="10" cy="10" r="6"/><path d="M14.5 14.5 20 20"/></svg></div>
    <p class="solution__title"><b>Heading</b> Goes Here</p>
    <p class="solution__text">Vivamus eu dui ex. Curabitur dapibus dignissim dui, in molest</p>
  </div>

  <div class="solution" style="left:67px;top:386px">
    <div class="badge badge--teal"><svg viewBox="0 0 24 24"><circle cx="12" cy="12" r="8"/><path d="M12 7v5l3 2"/></svg></div>
    <p class="solution__title"><b>Heading</b> Goes Here</p>
    <p class="solution__text">Vivamus eu dui ex. Curabitur dapibus dignissim dui, in molest</p>
  </div>
  <div class="solution" style="left:460px;top:386px">
    <div class="badge badge--navy"><svg viewBox="0 0 24 24"><circle cx="12" cy="8" r="3"/><circle cx="6" cy="10" r="2.2"/><circle cx="18" cy="10" r="2.2"/><path d="M7 19c0-3 2-5 5-5s5 2 5 5M2.5 18c0-2 1.5-4 3.5-4M21.5 18c0-2-1.5-4-3.5-4"/></svg></div>
    <p class="solution__title"><b>Heading</b> Goes Here</p>
    <p class="solution__text">Vivamus eu dui ex. Curabitur dapibus dignissim dui, in molest</p>
  </div>
  <div class="solution" style="left:853px;top:386px">
    <div class="badge badge--yellow"><svg viewBox="0 0 24 24"><path d="M5 20v-5M10 20v-8M15 20v-6M20 20V9M4 10l5-4 4 3 6-5M16 4h3v3"/></svg></div>
    <p class="solution__title"><b>Heading</b> Goes Here</p>
    <p class="solution__text">Vivamus eu dui ex. Curabitur dapibus dignissim dui, in molest</p>
  </div>

  <div class="brand brand--footer"><span class="brand__dot"></span>Corvanta</div>
  <div class="page-footer"><span>© 2022 Corvanta Learning, All rights reserved.</span><span class="page-footer__num">2</span></div>
</section>

<!-- Values slide -->
<section class="slide slide--values">
  <h2 class="heading"><span><b>Corvanta</b> Values</span></h2>

  <div class="value" style="top:173px">
    <div class="badge badge--navy"><svg viewBox="0 0 24 24"><path d="M9 3h6M10 3v6l-5 9a2 2 0 0 0 1.8 3h10.4A2 2 0 0 0 19 18l-5-9V3M8 15h8"/></svg></div>
    <div><p class="value__title">we love <b>innovations</b></p>
    <p class="value__text">Lorem ipsum dolor sit amet, consectetur adipiscing elit. Vivamus eu dui ex. Curabitur dapibus dignissim dui, in molestie metus feugiat sed. Praesent aliquet lorem ex, eu dapibus odio varius at. Duis eget tellus porta, consequat lacus vitae, venenatis dolor.</p></div>
  </div>
  <div class="value" style="top:318px">
    <div class="badge badge--yellow"><svg viewBox="0 0 24 24"><path d="M12 21v-7M12 14l-3-2M12 16l3-3M8 14a4 4 0 0 1-1-7.5A5 5 0 0 1 17 6.5 4 4 0 0 1 16 14z"/></svg></div>
    <div><p class="value__title">we respect the <b>nature</b></p>
    <p class="value__text">Lorem ipsum dolor sit amet, consectetur adipiscing elit. Vivamus eu dui ex. Curabitur dapibus dignissim dui, in molestie metus feugiat sed. Praesent aliquet lorem ex, eu dapibus odio varius at. Duis eget tellus porta, consequat lacus vitae, venenatis dolor.</p></div>
  </div>
  <div class="value" style="top:463px">
    <div class="badge badge--teal"><svg viewBox="0 0 24 24"><path d="M14 4c3-1 6-1 6-1s0 3-1 6l-6 6-4-4 5-7zM9 11l-4 1-2 3 4 1M13 15l-1 4-3 2-1-4M15 9h.01"/></svg></div>
    <div><p class="value__title">we believe in <b>future</b></p>
    <p class="value__text">Lorem ipsum dolor sit amet, consectetur adipiscing elit. Vivamus eu dui ex. Curabitur dapibus dignissim dui, in molestie metus feugiat sed. Praesent aliquet lorem ex, eu dapibus odio varius at. Duis eget tellus porta, consequat lacus vitae, venenatis dolor.</p></div>
  </div>

  <div class="brand brand--footer"><span class="brand__dot"></span>Corvanta</div>
  <div class="page-footer"><span>© 2022 Corvanta Learning, All rights reserved.</span><span class="page-footer__num">3</span></div>
</section>

<!-- Contact slide -->
<section class="slide slide--contact">
  <div class="photo photo--towers" role="img" aria-label="Photo looking up at glass office towers against a pale sky"></div>
  <div class="tint tint--teal"></div>
  <div class="tint tint--yellow" style="top:368px;height:214px"></div>
  <div class="brand brand--contact"><span class="brand__dot"></span>Corvanta</div>
  <div class="contact">
    <p class="contact__title">Contact Us</p>
    <p class="contact__row"><svg viewBox="0 0 24 24"><path d="M5 4h4l2 5-2.5 1.5a11 11 0 0 0 5 5L15 13l5 2v4a2 2 0 0 1-2 2A16 16 0 0 1 3 6a2 2 0 0 1 2-2z"/></svg>Phone Number Goes Here</p>
    <p class="contact__row"><svg viewBox="0 0 24 24"><circle cx="12" cy="12" r="4"/><path d="M16 8v5a3 3 0 0 0 6 0v-1a10 10 0 1 0-4 8"/></svg>E-Mail Address Goes Here</p>
    <p class="contact__row"><svg viewBox="0 0 24 24"><circle cx="12" cy="12" r="9"/><path d="M3 12h18M12 3a14 14 0 0 1 0 18M12 3a14 14 0 0 0 0 18"/></svg>URL Address Goes Here</p>
  </div>
  <footer class="band">© 2022 Corvanta Learning, All rights reserved.</footer>
</section>

</body>
</html>
```